PowerPoint template for Credit Card Processor

We need a powerpoint template for our new credit card processing company. Our goal is to sign up merchants to accept credit cards. We will be making presentations to merchants to get them to sign up for our services.

We already have a logo designed. We'd like to incorporate that logo and color scheme in the powerpoint template. The logo file is an illustrator file.

I generally like light colored backgrounds. Nothing too dark.

Credit Card

• our logo

```html
<!DOCTYPE html>
<html lang="en">
<head>
<meta charset="utf-8">
<title>Tallyway.net Presentation Template</title>
<link rel="stylesheet" href="https://fonts.googleapis.com/css2?family=Source+Sans+3:wght@300;400;600;700&display=swap">
<style>
  :root {
    --navy: #1a4f7c;
    --blue: #1f8fc3;
    --cyan: #8fd3e6;
    --bright: #12a0cf;
    --title: #1a8fc6;
    --ink: #6b6b6b;
    --brand-grey: #555a60;
    --stage: #000000;
    --white: #ffffff;
  }
  * { box-sizing: border-box; margin: 0; padding: 0; }
  html, body { width: 1200px; height: 900px; overflow: hidden; background: var(--stage); }
  body { position: relative; font-family: "Source Sans 3", sans-serif; }

  .slide { position: absolute; width: 475px; height: 367px; overflow: hidden; }
  .slide--cover   { left: 110px; top: 70px;  background: var(--navy); }
  .slide--content { background: radial-gradient(ellipse at 50% 40%, #ffffff 0%, #ececec 100%); }
  .slide--photo   { left: 596px; top: 70px; }
  .slide--chart   { left: 111px; top: 466px; }
  .slide--closing { left: 596px; top: 466px; background: var(--navy); }

  .waves { position: absolute; left: 0; top: 0; width: 475px; height: 367px; }

  .brand { position: absolute; display: flex; align-items: center; gap: 6px; color: var(--brand-grey); font-weight: 400; white-space: nowrap; }
  .brand__dot { width: 0.7em; height: 0.7em; border-radius: 50%; background: var(--blue); }

  /* cover */
  .cover__heading { position: absolute; right: 34px; top: 120px; text-align: right; color: var(--white); }
  .cover__welcome { font-size: 25px; font-weight: 700; line-height: 1.2; }
  .cover__sub { font-size: 25px; font-weight: 300; line-height: 1.2; }
  .cover__date { font-size: 13.5px; font-weight: 400; margin-top: 6px; }
  .slide--cover .brand { right: 34px; top: 302px; font-size: 26px; }

  /* content header */
  .slide-header .brand { left: 22px; top: 26px; font-size: 17px; }
  .slide-header__rule { position: absolute; left: 148px; right: 24px; top: 41px; height: 1px; background: #b9b9b9; }
  .slide-header__title { position: absolute; right: 24px; top: 21px; color: var(--title); font-size: 16px; font-weight: 400; letter-spacing: 0.2px; }

  .body-copy { position: absolute; color: var(--ink); font-size: 8.8px; font-weight: 300; line-height: 16.8px; }
  .body-copy p + p { margin-top: 16.8px; }
  .body-copy--justified { text-align: justify; }

  .photo-frame { position: absolute; left: 49px; top: 82px; width: 102px; height: 122px; background: var(--white); padding: 5px; box-shadow: 0 3px 5px rgba(0,0,0,0.35); }
  .photo-frame__fill { width: 100%; height: 100%; background: linear-gradient(160deg, #c9d3dc 0%, #7d8791 55%, #2c2f34 100%); }

  .pie { position: absolute; left: 0; top: 0; }

  .page-number { position: absolute; right: 14px; bottom: 8px; color: var(--white); font-size: 6.5px; }

  /* closing */
  .slide--closing .brand { left: 50%; top: 166px; transform: translateX(-50%); font-size: 25px; color: var(--white); }
  .slide--closing .brand__dot { background: var(--cyan); }
  .closing__contact { position: absolute; left: 0; right: 0; top: 322px; text-align: center; color: var(--white); font-size: 7px; line-height: 8.8px; }
</style>
</head>
<body>

<section class="slide slide--cover">
  <svg class="waves" viewBox="0 0 475 367" preserveAspectRatio="none" aria-hidden="true">
    <path d="M0 288 Q220 238 475 262 L475 367 L0 367 Z" fill="var(--blue)"/>
    <path d="M0 300 Q180 250 475 282 L475 367 L0 367 Z" fill="var(--cyan)"/>
    <path d="M0 318 Q230 258 475 286 L475 360 L0 360 Z" fill="#ffffff"/>
    <rect x="0" y="360" width="475" height="7" fill="var(--navy)"/>
  </svg>
  <div class="cover__heading">
    <div class="cover__welcome">WELCOME</div>
    <div class="cover__sub">TO OUR PRESENTATION</div>
    <div class="cover__date">Birmingham, August 25, 2013</div>
  </div>
  <div class="brand"><span class="brand__dot"></span>Tallyway.net</div>
</section>

<section class="slide slide--content slide--photo">
  <header class="slide-header">
    <div class="brand"><span class="brand__dot"></span>Tallyway.net</div>
    <div class="slide-header__rule"></div>
    <h2 class="slide-header__title">PRESENTATION TITLE</h2>
  </header>
  <figure class="photo-frame"><div class="photo-frame__fill" role="img" aria-label="Photo of a smiling business team"></div></figure>
  <div class="body-copy" style="left:166px; top:97px; width:250px;">
    <p>Lorem ipsum dolor sit amet, consectetur adipisicing elit, sed do eiusmod tempor incididunt ut labore et dolore magna aliqua. Ut enim ad minim veniam, quis nostrud exercitation ullamco laboris nisi ut aliquip ex ea commodo consequat. Duis aute irure dolor in reprehenderit in voluptate velit esse cillum dolore eu fugiat nulla pariatur.</p>
  </div>
  <div class="body-copy" style="left:48px; top:219px; width:368px;">
    <p>Lorem ipsum dolor sit amet, consectetur adipisicing elit, sed do eiusmod tempor incididunt ut labore et dolore magna aliqua. Ut enim ad minim veniam, quis nostrud exercitation ullamco laboris nisi ut aliquip ex ea commodo consequat. Duis aute irure dolor in reprehenderit in voluptate velit esse cillum dolore eu fugiat nulla pariatur.</p>
  </div>
  <svg class="waves" viewBox="0 0 475 367" preserveAspectRatio="none" aria-hidden="true">
    <path d="M0 325 Q280 352 475 303 L475 367 L0 367 Z" fill="var(--cyan)"/>
    <path d="M0 330 Q240 350 475 332 L475 367 L0 367 Z" fill="var(--blue)"/>
    <path d="M0 343 Q260 358 475 342 L475 367 L0 367 Z" fill="var(--navy)"/>
  </svg>
  <span class="page-number">2</span>
</section>

<section class="slide slide--content slide--chart">
  <header class="slide-header">
    <div class="brand"><span class="brand__dot"></span>Tallyway.net</div>
    <div class="slide-header__rule"></div>
    <h2 class="slide-header__title">PRESENTATION TITLE</h2>
  </header>
  <svg class="pie" width="475" height="367" viewBox="0 0 475 367" aria-label="Pie chart">
    <defs><filter id="pie-shadow"><feGaussianBlur stdDeviation="3"/></filter></defs>
    <ellipse cx="110" cy="297" rx="84" ry="4" fill="#8a8a8a" opacity="0.55" filter="url(#pie-shadow)"/>
    <path d="M28 215 L28 229 A82 58 0 0 0 192 229 L192 215 Z" fill="#2b2b2b"/>
    <path d="M110 215 L110 157 A82 58 0 0 1 138 269.5 Z" fill="var(--navy)"/>
    <path d="M110 215 L138 269.5 A82 58 0 0 1 30.8 230 Z" fill="#5c5c5c"/>
    <path d="M110 215 L30.8 230 A82 58 0 0 1 42.8 181.7 Z" fill="#7f7f7f"/>
    <path d="M110 215 L42.8 181.7 A82 58 0 0 1 75.3 162.4 Z" fill="var(--cyan)"/>
    <path d="M110 215 L75.3 162.4 A82 58 0 0 1 110 157 Z" fill="var(--bright)"/>
  </svg>
  <div class="body-copy body-copy--justified" style="left:222px; top:70px; width:219px;">
    <p>Lorem ipsum dolor sit amet, consectetur adipisicing elit, sed do eiusmod tempor incididunt ut labore et dolore magna aliqua. Ut enim ad minim veniam, quis nostrud exercitation ullamco laboris nisi ut aliquip ex ea commodo consequat. Duis aute irure dolor in reprehenderit in voluptate velit esse cillum dolore eu fugiat nulla pariatur.</p>
    <p>Lorem ipsum dolor sit amet, consectetur adipisicing elit, sed do eiusmod tempor incididunt ut labore et dolore magna aliqua. Ut enim ad minim veniam, quis nostrud exercitation ullamco laboris nisi ut aliquip ex ea commodo consequat. Duis aute irure dolor in reprehenderit in voluptate velit esse cillum dolore eu fugiat nulla pariatur.</p>
  </div>
  <svg class="waves" viewBox="0 0 475 367" preserveAspectRatio="none" aria-hidden="true">
    <path d="M0 325 Q280 352 475 303 L475 367 L0 367 Z" fill="var(--cyan)"/>
    <path d="M0 330 Q240 350 475 332 L475 367 L0 367 Z" fill="var(--blue)"/>
    <path d="M0 343 Q260 358 475 342 L475 367 L0 367 Z" fill="var(--navy)"/>
  </svg>
  <span class="page-number">2</span>
</section>

<section class="slide slide--closing">
  <div class="brand"><span class="brand__dot"></span>Tallyway.net</div>
  <address class="closing__contact" style="font-style:normal;">
    1180 Harbor Lane, #214 Westfield, NY&nbsp; 14700<br>
    Phone. 5550142&nbsp; Fax. 5550143<br>
    www.tallyway.net
  </address>
</section>

</body>
</html>
```